Monthly Planner & To Do List on dry erase magnetic whiteboard

I'm after 2 x designs for magnetic whiteboards.
1. 17 x 13 inches is a monthly planner. Dates and month can be written in each month and then wiped off and re-written for the next month.
2. 6 x 4 inches - to do list however I don't want this to say To Do on it but will have lines to write on and possibly bullet points to check off.
I have attached below samples of other products (the ones I like the most are the first two - 9.19.52 and 9.20.34). I actually don't like the design of the others but just show them here as an example for layout purposes.
I want something that is modern, slick, simple yet stylish which is what my brand is representative of - smart, modern, organised. It will be printed onto a white board and I only want the print to be in black, no grey shading. I need a more modern font and don't like any of the swirly parts. Just clean and simple but slick.
I would like the size of the day squares to be as large as possible to fit writing in them and also for a section somewhere on the page for additional notes.

• Old style fonts, cartoon style or childish.

```html
<!DOCTYPE html>
<html lang="en">
<head>
<meta charset="utf-8">
<title>Memo – Monthly List</title>
<link rel="stylesheet" href="https://fonts.googleapis.com/css2?family=Quicksand:wght@400;500&family=Shadows+Into+Light+Two&display=swap">
<style>
  :root {
    --ink: #111111;
    --paper: #ffffff;
    --rule: #222222;
  }
  html, body {
    margin: 0;
    padding: 0;
    overflow: hidden;
    background: var(--paper);
  }
  .board {
    position: relative;
    width: 800px;
    height: 1200px;
    background: var(--paper);
    overflow: hidden;
    color: var(--ink);
  }
  .board__title {
    position: absolute;
    left: 26px;
    top: 22px;
    margin: 0;
    font-family: "Quicksand", sans-serif;
    font-weight: 500;
    font-size: 46px;
    letter-spacing: 1px;
    line-height: 1;
  }
  .board__month {
    position: absolute;
    left: 414px;
    top: 30px;
    display: flex;
    align-items: baseline;
    font-family: "Quicksand", sans-serif;
    font-weight: 500;
    font-size: 42px;
    line-height: 1;
  }
  .board__month-blank {
    display: inline-block;
    width: 172px;
    margin-left: 4px;
    border-bottom: 2px dotted var(--ink);
  }
  .ruling {
    position: absolute;
    inset: 0;
  }
  .ruling line {
    stroke: var(--rule);
    stroke-width: 2;
  }
  .entries {
    list-style: none;
    margin: 0;
    padding: 0;
  }
  .entry {
    position: absolute;
    left: 26px;
    display: flex;
    align-items: center;
    font-family: "Shadows Into Light Two", cursive;
    font-size: 31px;
    line-height: 1;
  }
  .entry__bullet {
    width: 10px;
    height: 10px;
    border: 2px solid var(--ink);
    border-radius: 50%;
    margin-right: 46px;
    margin-top: 8px;
    flex: none;
  }
</style>
</head>
<body>
<main class="board">
  <h1 class="board__title">memo</h1>
  <div class="board__month">month<span class="board__month-blank"></span></div>

  <svg class="ruling" width="800" height="1200" viewBox="0 0 800 1200" aria-hidden="true">
    <line x1="22" y1="167" x2="752" y2="167"/>
    <line x1="22" y1="218" x2="752" y2="218"/>
    <line x1="22" y1="270" x2="752" y2="270"/>
    <line x1="22" y1="321" x2="752" y2="321"/>
    <line x1="22" y1="373" x2="752" y2="373"/>
    <line x1="22" y1="454" x2="752" y2="454"/>
    <line x1="22" y1="535" x2="752" y2="535"/>
    <line x1="22" y1="616" x2="752" y2="616"/>
    <line x1="22" y1="697" x2="752" y2="697"/>
    <line x1="22" y1="778" x2="752" y2="778"/>
    <line x1="22" y1="859" x2="752" y2="859"/>
    <line x1="22" y1="940" x2="752" y2="940"/>
    <line x1="22" y1="1018" x2="752" y2="1018"/>
  </svg>

  <ul class="entries">
    <li class="entry" style="top:128px"><span class="entry__bullet"></span>Lorem ipsum dolor</li>
    <li class="entry" style="top:179px"><span class="entry__bullet"></span>fugiat nulla pariatur</li>
    <li class="entry" style="top:230px"><span class="entry__bullet"></span>nostrud exercitation</li>
    <li class="entry" style="top:282px"><span class="entry__bullet"></span>aliquip ex ea commodo consequat</li>
    <li class="entry" style="top:333px"><span class="entry__bullet"></span>qui officia deserunt mollit</li>
  </ul>
</main>
</body>
</html>
```